依頼詳細
※ワイヤーフレームは以下よりダウンロードしてください
https://52.filokura.example/0714-e2f19c7a0d4b8e61a3c5f0d9b7e24a6c1f

※画像素材はピクソラフォトを使用してください

■サイトマップ
1 TOP
2 会社情報
3 企業理念
4 代表あいさつ
5 社員紹介(一覧)
6 プライバシーポリシー
7 事業内容
8 ツアーの流れ
9 採用情報
10 目的別の旅行先(一覧)
11 目的別の旅行先(詳細)
12 日本の旅行先(一覧)
13 日本の旅行先(詳細)
14 コラム(一覧)
15 コラム(詳細)
16 よくある質問(一覧)
17 お客様の声(一覧)
18 お客様の声(詳細)
19 お問い合わせ

■参考サイト(※現行サイト、ポータルサイトなど)
・現行サイト
https://www.kumotabi-ryoko.co.jp/

・参考サイト
https://www.hoshizoratrips.jp/company/
└レイアウトを参考にしていただきたいです。

https://www.lodgeqmr.com/lumieresquare/
└上記サイトのようにMVをフルディスプレイにして、
飛行機の写真を使用していただきたいです。

■カラー
白ベースで、ポイントや背景画像に青系を使用してください。
以下のサイトの色味を参考にしてください。
https://www.sorafune-tec.co.jp/

■フォントについて
・無料で使えるフォントで作成お願い致します
・OSに紐づくフォントの使用は控えていただければと思います (ヒラギノなど)

■文章について
・可能な限り「ダミーテキスト」を繰り返した文字の配置は避けて頂きたいです

■ワイヤーフレーム
こちらを参考にしていただきたいです。
デザインなどはお任せいたします。
ページ数
1ページ
希望イメージ
シンプル 複雑
単色 カラフル
暗い 明るい
日常 高級
遊び心 厳粛
未来的 伝統的
女性的 男性的
希望する色
青系
納品ファイル
• イラストレーター形式 (.ai)
• フォトショップ形式 (.psd)
補足説明
◆素材について
Pixora Photo画像をご使用ください。
その際、通常アセットでダウンロード出来る画像のみを使用してください。
Pixora Photo以外の素材を使用する際には、
必ず無料で提供いただける物のみご使用ください。

◆ワイヤーフレームについて
絶対に厳守していただく必要はございません。
デザイン的にこちらの方が良いなどあれば、
そちらを採用してください

◆サイズについて
TOPデザイン自体の画像サイズは、横幅1300pxで提案をお願いできますと幸いです。(縦幅の制限はございません)

※通常業務へ支障が出るため、店舗へのお電話はお控え下さい。
もう少し提案を見させて頂きたい為、期間を延長いたします。
皆様のご提案をお待ちしております。

```html
<!DOCTYPE html>
<html lang="ja">
<head>
<meta charset="UTF-8">
<title>ソラノミチツアー | あなたの旅を本気でサポートする会社。</title>
<link href="https://fonts.googleapis.com/css2?family=Noto+Sans+JP:wght@400;500;700&family=Montserrat:wght@500;600;700&family=Great+Vibes&display=swap" rel="stylesheet">
<style>
:root{
  --blue:#1b4fb3;
  --navy:#0f2f7a;
  --deep:#0a2463;
  --sky:#3d7be0;
  --pale:#e3ecf9;
  --pale2:#f2f6fc;
  --text:#1f2a44;
  --muted:#6b7a99;
  --white:#ffffff;
  --line:#c9d6ec;
}
*{margin:0;padding:0;box-sizing:border-box}
html,body{width:1200px;height:4912px;overflow:hidden}
body{position:relative;background:var(--white);color:var(--text);font-family:"Noto Sans JP",sans-serif}
.abs{position:absolute}
.en{font-family:"Montserrat",sans-serif;letter-spacing:.12em}
.ph{position:absolute}

/* header */
.site-header{left:0;top:0;width:1200px;height:70px;display:flex;align-items:center;justify-content:space-between;padding:0 40px;z-index:5}
.brand{display:flex;align-items:center;gap:10px;color:var(--white);font-weight:700;font-size:18px}
.brand-mark{width:22px;height:22px;border-radius:50%;background:var(--white)}
.global-nav{display:flex;gap:28px;font-size:13px;color:var(--white);font-weight:500}

/* hero */
.hero-photo{left:0;top:0;width:1200px;height:560px;background:linear-gradient(180deg,#2a4585 0%,#6f6e9e 35%,#d99a86 65%,#f2c39b 100%)}
.hero-script{left:800px;top:110px;font-family:"Great Vibes",cursive;font-size:62px;color:var(--white);transform:rotate(-8deg)}
.hero-copy{left:820px;top:280px;color:var(--white);font-size:30px;font-weight:700;line-height:1.55;letter-spacing:.05em;text-shadow:0 2px 10px rgba(0,0,0,.25)}

/* contact strip */
.cta-band{left:0;top:470px;width:1020px;height:170px;background:linear-gradient(100deg,var(--deep),var(--blue));clip-path:polygon(0 0,100% 0,92% 100%,0 100%)}
.cta-label{top:488px;color:var(--white);font-size:14px;font-weight:700}
.cta-box{top:520px;height:70px;background:var(--white);display:flex;align-items:center;gap:14px;padding:0 26px;box-shadow:0 6px 18px rgba(10,36,99,.2)}
.cta-box .txt{font-size:17px;font-weight:700;color:var(--navy)}
.cta-box small{display:block;font-size:11px;color:var(--muted);font-weight:500}
.cta-box .tel{font-family:"Montserrat",sans-serif;font-size:28px;font-weight:700;color:var(--navy);letter-spacing:.02em}

/* section headings */
.sec-title{font-size:30px;font-weight:700;letter-spacing:.06em}
.sec-en{font-size:12px;font-weight:600;margin-top:4px}
.btn-more{display:flex;align-items:center;justify-content:space-between;width:170px;height:40px;padding:0 18px;background:var(--white);color:var(--navy);font-family:"Montserrat",sans-serif;font-size:12px;font-weight:700;letter-spacing:.08em;box-shadow:0 4px 12px rgba(10,36,99,.18)}
.btn-more::after{content:"";border-left:7px solid currentColor;border-top:5px solid transparent;border-bottom:5px solid transparent}

/* news */
.news-panel{left:0;top:640px;width:470px;height:380px;background:linear-gradient(150deg,var(--sky),var(--blue));clip-path:polygon(0 0,100% 0,60% 100%,0 100%)}
.news-head{left:90px;top:730px;color:var(--white)}
.news-list{left:470px;top:700px;width:660px;list-style:none}
.news-list li{display:flex;gap:28px;padding:22px 0;border-bottom:1px solid var(--line);font-size:14px;line-height:1.8}
.news-list time{font-family:"Montserrat",sans-serif;font-weight:600;color:var(--blue);font-size:13px;flex:none;padding-top:2px}

/* booking */
.booking-bg{left:0;top:1020px;width:1200px;height:740px;background:linear-gradient(125deg,var(--blue) 0%,var(--sky) 45%,var(--blue) 70%,var(--navy) 100%)}
.booking-ill{left:540px;top:1100px;width:230px;height:170px;background:linear-gradient(160deg,#f4f7fc,#b9cdee);border-radius:4px}
.booking-head{left:800px;top:1190px;color:var(--white)}
.slides{left:0;top:1300px;width:1200px;height:360px}
.slide{position:absolute;top:0;height:360px}
.slide-name{position:absolute;left:20px;top:140px;color:var(--white);font-family:"Montserrat",sans-serif;font-weight:700;font-size:26px;letter-spacing:.1em;text-shadow:0 2px 8px rgba(0,0,0,.35)}
.slide-btn{position:absolute;left:150px;top:240px;width:120px;height:36px;background:var(--white);color:var(--navy);font-size:13px;font-weight:700;display:flex;align-items:center;justify-content:center;gap:10px}
.dots{left:0;top:1700px;width:1200px;display:flex;justify-content:center;gap:12px}
.dots span{width:14px;height:14px;border-radius:50%;border:2px solid var(--white)}
.dots span.on{background:var(--white)}

/* business */
.biz-bg{left:0;top:1760px;width:1200px;height:1000px;background:var(--pale)}
.biz-photo{left:640px;top:1760px;width:560px;height:1000px;background:linear-gradient(170deg,#c6b79a,#8e9a74 50%,#d8d0bf);clip-path:polygon(40% 0,100% 0,100% 100%)}
.biz-ill{left:220px;top:1780px;width:130px;height:110px;background:linear-gradient(160deg,#ffffff,#c3d4ef);border-radius:4px}
.biz-head{left:60px;top:1900px;color:var(--text)}
.biz-head .sec-en{color:var(--blue)}
.biz-card{position:absolute;width:300px;height:230px;background:var(--white);transform:skewX(-14deg);box-shadow:0 6px 18px rgba(10,36,99,.1)}
.biz-card .inner{transform:skewX(14deg);height:100%;display:flex;flex-direction:column;align-items:center;justify-content:center;gap:18px;color:var(--navy);font-size:15px;font-weight:700;text-align:center;line-height:1.5}

/* media */
.media-photo{left:0;top:2760px;width:1200px;height:520px;background:linear-gradient(160deg,#dbe3ee,#b8c7dc 50%,#8ea6c6)}
.media-white{left:0;top:3000px;width:1200px;height:520px;background:var(--white);clip-path:polygon(0 30%,100% 0,100% 100%,0 100%)}
.media-ill{left:820px;top:2790px;width:90px;height:120px;background:linear-gradient(#e8efe0,#9fb98a);border-radius:4px}
.media-head{left:900px;top:2870px;color:var(--text)}
.media-head .sec-en{color:var(--blue)}
.media-card{position:absolute;top:3020px;width:290px}
.media-card .img{height:300px;display:flex;align-items:center;justify-content:center}
.media-card .cap{background:rgba(255,255,255,.9);padding:6px 14px;font-size:14px;font-weight:700;color:var(--navy)}
.media-card .more{height:56px;background:var(--blue);color:var(--white);font-family:"Montserrat",sans-serif;font-weight:700;font-size:13px;letter-spacing:.1em;display:flex;align-items:center;justify-content:center;gap:12px}
.media-card .more::after{content:"";border-left:7px solid var(--white);border-top:5px solid transparent;border-bottom:5px solid transparent}

/* faq */
.faq-side{left:1000px;top:3520px;width:200px;height:780px;background:linear-gradient(180deg,var(--sky),var(--navy));clip-path:polygon(60% 0,100% 0,100% 100%,0 100%)}
.faq-ill{left:350px;top:3550px;width:110px;height:150px;background:linear-gradient(#eef3fb,#b6c9ea);border-radius:4px}
.faq-head{left:60px;top:3620px}
.faq-head .sec-en{color:var(--blue)}
.faq-item{position:absolute;left:120px;width:960px;background:var(--white);box-shadow:0 4px 14px rgba(10,36,99,.12);font-size:14px}
.faq-row{display:flex;align-items:center;gap:18px;padding:0 26px;height:64px}
.faq-row b{font-family:"Montserrat",sans-serif;font-size:16px}
.faq-q b{color:var(--blue)}
.faq-a{border-top:1px solid var(--line);background:var(--pale2)}
.faq-a b{color:#d9465b}
.faq-row .tog{margin-left:auto;width:0;height:0;border-left:6px solid transparent;border-right:6px solid transparent}
.tog.up{border-bottom:8px solid var(--blue)}
.tog.down{border-top:8px solid var(--blue)}

/* footer */
.footer-top{left:0;top:4300px;width:1200px;height:612px;background:var(--white);border-top:1px solid var(--line)}
.footer-brand{left:60px;top:4345px;display:flex;align-items:center;gap:10px;font-weight:700;font-size:20px;color:var(--navy)}
.footer-brand .brand-mark{background:var(--navy)}
.footer-info{left:60px;top:4430px;font-size:13px;line-height:2;color:var(--text)}
.footer-info strong{font-size:15px}
.footer-col{position:absolute;top:4430px;font-size:13px;line-height:2.3;color:var(--text);list-style:none}
.footer-col li.head{font-weight:700;color:var(--navy)}
.footer-col li.sub::before{content:"・"}
.footer-bar{left:0;top:4872px;width:1200px;height:40px;background:var(--navy);color:var(--white);font-size:11px;display:flex;align-items:center;justify-content:center;font-family:"Montserrat",sans-serif;letter-spacing:.08em}
</style>
</head>
<body>

<!-- Hero -->
<div class="ph hero-photo" role="img" aria-label="夕焼け空を飛ぶ旅客機の写真"></div>
<header class="abs site-header">
  <div class="brand"><span class="brand-mark"></span>ソラノミチツアー</div>
  <nav class="global-nav"><span>会社情報</span><span>事業案内</span><span>ツアーの流れ</span><span>採用情報</span><span>お客様の声</span><span>お問い合わせ</span></nav>
</header>
<p class="abs hero-script">Travel Freely</p>
<h1 class="abs hero-copy">あなたの旅を<br>本気でサポートする会社。</h1>

<!-- CTA -->
<div class="abs cta-band"></div>
<p class="abs cta-label" style="left:250px">今すぐ旅行に行きたい</p>
<p class="abs cta-label" style="left:640px">電話で問い合わせしたい</p>
<a class="abs cta-box" style="left:150px;width:390px">
  <svg width="30" height="30" viewBox="0 0 30 30" fill="none" stroke="#1b4fb3" stroke-width="2"><rect x="5" y="4" width="20" height="23" rx="2"/><path d="M10 11h10M10 16h10M10 21h6"/></svg>
  <span class="txt">ツアー予約ページへ飛ぶ</span>
</a>
<a class="abs cta-box" style="left:560px;width:400px">
  <svg width="30" height="30" viewBox="0 0 30 30" fill="none" stroke="#1b4fb3" stroke-width="2"><circle cx="15" cy="15" r="13"/><path d="M10 9c0 6 5 11 11 11l1.5-3-3-1.5-1.5 1.5c-2-1-3.5-2.5-4.5-4.5l1.5-1.5L13.5 8z"/></svg>
  <span><small>お客様相談窓口</small><span class="tel">06-4512-7730</span></span>
</a>

<!-- News -->
<div class="abs news-panel"></div>
<div class="abs news-head" style="color:#fff">
  <h2 class="sec-title">新着情報</h2>
  <p class="en sec-en">NEWS</p>
  <a class="btn-more" style="margin-top:40px">VIEW MORE</a>
</div>
<ul class="abs news-list">
  <li><time>2021/10/01</time><span>秋の国内ツアー特集を公開しました。紅葉の名所を巡る日帰りプランから温泉旅館の宿泊プランまで幅広くご紹介しています。</span></li>
  <li><time>2021/10/01</time><span>年末年始の窓口営業時間についてのお知らせです。期間中のお問い合わせはお早めにお願いいたします。</span></li>
  <li><time>2021/10/01</time><span>法人様向け出張手配サービスの受付を開始しました。航空券と宿泊のまとめて手配が可能です。</span></li>
</ul>

<!-- Booking -->
<div class="abs booking-bg"></div>
<div class="ph booking-ill" role="img" aria-label="パソコンで旅行を予約する人物のイラスト"></div>
<div class="abs booking-head">
  <h2 class="sec-title">今すぐ旅行を予約する</h2>
  <p class="en sec-en">BOOKING</p>
</div>
<div class="abs slides">
  <div class="slide" style="left:0;width:215px;background:linear-gradient(160deg,#7d9bb0,#4f6e3e)" role="img" aria-label="北海道の海岸と草原の写真"><span class="slide-name" style="left:-20px">HOKKAIDO</span></div>
  <div class="slide" style="left:215px;width:365px;background:linear-gradient(160deg,#a7b6c4,#6f7a80 60%,#8a8f86)" role="img" aria-label="沖縄のシーサー像と空の写真"><span class="slide-name">OKINAWA</span></div>
  <div class="slide" style="left:580px;width:320px;background:linear-gradient(160deg,#9fc0e6,#5f8a4f 60%,#7b6b58)" role="img" aria-label="緑に囲まれた洋館の写真"><span class="slide-btn">予約する<svg width="8" height="10"><path d="M0 0l8 5-8 5z" fill="#0f2f7a"/></svg></span></div>
  <div class="slide" style="left:900px;width:50px;background:linear-gradient(#c9a27a,#7a5a40)" role="img" aria-label="観光地の写真"></div>
  <div class="slide" style="left:950px;width:250px;background:linear-gradient(160deg,#8c2b2b,#c45a3a 50%,#3d4a3a)" role="img" aria-label="赤い五重塔の写真"></div>
</div>
<div class="abs dots"><span></span><span></span><span></span><span></span><span></span><span class="on"></span><span></span><span></span></div>

<!-- Business -->
<div class="abs biz-bg"></div>
<div class="ph biz-photo" role="img" aria-label="石造りの街並みの写真"></div>
<div class="ph biz-ill" role="img" aria-label="会議をする人々のイラスト"></div>
<div class="abs biz-head">
  <h2 class="sec-title">事業内容</h2>
  <p class="en sec-en">BUSINESS</p>
</div>
<div class="biz-card" style="left:170px;top:2060px"><div class="inner">
  <svg width="64" height="64" viewBox="0 0 64 64" fill="none" stroke="#1b4fb3" stroke-width="3"><path d="M32 6v52M18 14h26l6 6-6 6H18zM46 32H22l-6 6 6 6h24z"/></svg>ダイナミック<br>パッケージ</div></div>
<div class="biz-card" style="left:480px;top:2060px"><div class="inner">
  <svg width="64" height="64" viewBox="0 0 64 64" fill="none" stroke="#1b4fb3" stroke-width="3"><circle cx="30" cy="34" r="22"/><path d="M8 34h44M30 12c-8 8-8 36 0 44M30 12c8 8 8 36 0 44M44 8l12 4-8 8"/></svg>国内・海外旅行</div></div>
<div class="biz-card" style="left:790px;top:2060px"><div class="inner">
  <svg width="64" height="64" viewBox="0 0 64 64" fill="none" stroke="#1b4fb3" stroke-width="3"><rect x="8" y="16" width="40" height="30" rx="3"/><path d="M8 26h40M36 40l12-6 10 2-6 6-12 4z"/></svg>法人出張</div></div>
<div class="biz-card" style="left:170px;top:2320px"><div class="inner">
  <svg width="64" height="64" viewBox="0 0 64 64" fill="none" stroke="#1b4fb3" stroke-width="3"><path d="M18 22h28M22 22a10 10 0 0 0 20 0M14 58c0-12 8-20 18-20s18 8 18 20zM20 20l4-12h16l4 12"/></svg>プランアドバイス</div></div>
<div class="biz-card" style="left:480px;top:2320px"><div class="inner">
  <svg width="64" height="64" viewBox="0 0 64 64" fill="none" stroke="#1b4fb3" stroke-width="3"><path d="M10 40v-10l6-14h32l6 14v10zM10 40v8h8v-8M46 40v8h8v-8M16 30h32"/><circle cx="20" cy="35" r="2"/><circle cx="44" cy="35" r="2"/></svg>インセンティブツアー</div></div>
<div class="biz-card" style="left:790px;top:2320px"><div class="inner">
  <svg width="64" height="64" viewBox="0 0 64 64" fill="none" stroke="#1b4fb3" stroke-width="3"><path d="M12 8h28l10 10v38H12zM20 26h20M20 34h20M20 42h12M36 50l18-18 4 4-18 18h-4z"/></svg>海外研修旅行</div></div>
<a class="abs btn-more" style="left:470px;top:2630px">VIEW MORE</a>

<!-- Media -->
<div class="ph media-photo" role="img" aria-label="ノートパソコンとノートが置かれたデスクの写真"></div>
<div class="abs media-white"></div>
<div class="ph media-ill" role="img" aria-label="観葉植物のイラスト"></div>
<div class="abs media-head">
  <h2 class="sec-title">自社メディア</h2>
  <p class="en sec-en">MEDIA</p>
</div>
<div class="media-card" style="left:130px">
  <div class="img" role="img" aria-label="旅行鞄とカメラの写真" style="background:linear-gradient(160deg,#7a6a5c,#b3a28f)"><span class="cap">目的別に旅行先を探す</span></div>
  <a class="more">VIEW MORE</a>
</div>
<div class="media-card" style="left:455px">
  <div class="img" role="img" aria-label="富士山と五重塔の写真" style="background:linear-gradient(180deg,#4d6fa8,#c77a6a 60%,#6a4a50)"><span class="cap">日本の旅行先を探す</span></div>
  <a class="more">VIEW MORE</a>
</div>
<div class="media-card" style="left:780px">
  <div class="img" role="img" aria-label="本とコーヒーカップの写真" style="background:linear-gradient(160deg,#e8e2d6,#b7a88f)"><span class="cap">コラム</span></div>
  <a class="more">VIEW MORE</a>
</div>

<!-- FAQ -->
<div class="ph faq-side" role="img" aria-label="青く光る高層ビルの写真"></div>
<div class="ph faq-ill" role="img" aria-label="質問ボードの前に立つ人物のイラスト"></div>
<div class="abs faq-head">
  <h2 class="sec-title">よくある質問</h2>
  <p class="en sec-en">FAQ</p>
</div>
<div class="faq-item" style="top:3740px">
  <div class="faq-row faq-q"><b>Q.</b><span>予約後に旅行日程を変更することはできますか？出発日の何日前まで受け付けていますか？</span><i class="tog up"></i></div>
  <div class="faq-row faq-a"><b>A.</b><span>出発日の14日前までであれば変更を承ります。プランにより手数料が発生する場合がございますので窓口までご相談ください。</span></div>
</div>
<div class="faq-item" style="top:3920px">
  <div class="faq-row faq-q"><b>Q.</b><span>店舗に行かずに電話やメールだけで旅行の申し込みをすることはできますか？</span><i class="tog down"></i></div>
</div>
<div class="faq-item" style="top:4040px">
  <div class="faq-row faq-q"><b>Q.</b><span>団体旅行や社員旅行など大人数での旅行プランの相談にも対応していますか？</span><i class="tog down"></i></div>
</div>
<a class="abs btn-more" style="left:880px;top:4160px">VIEW MORE</a>

<!-- Footer -->
<footer>
<div class="abs footer-top"></div>
<div class="abs footer-brand"><span class="brand-mark"></span>ソラノミチツアー</div>
<div class="abs footer-info">
  <strong>【空路トラベルデスク】<br>株式会社クモタビ旅行</strong><br>
  〒530-0000<br>
  大阪市北区空見町2丁目5-8 ソラミビル4F<br>
  TEL：06-4512-7730<br>
  営業時間：平日9:30〜18:00<br>
  　　　　　土曜日9:30〜13:00<br>
  定休日：日曜日・祝日<br>
  大阪府知事登録旅行業第2-000号
</div>
<ul class="footer-col" style="left:480px"><li class="head">TOP</li><li class="head">会社情報</li><li class="sub">企業理念</li><li class="sub">代表あいさつ</li><li class="sub">社員紹介</li></ul>
<ul class="footer-col" style="left:630px"><li class="head">事業案内</li><li class="sub">ダイナミックパッケージ</li><li class="sub">国内・海外旅行</li><li class="sub">法人出張</li><li class="sub">プランアドバイス</li><li class="sub">インセンティブツアー</li><li class="sub">海外研修旅行</li></ul>
<ul class="footer-col" style="left:800px"><li class="head">目的別の旅行先</li><li class="head">日本の旅行先</li><li class="head">ツアーの流れ</li><li class="head">コラム</li></ul>
<ul class="footer-col" style="left:960px"><li class="head">採用情報</li><li class="head">よくある質問</li><li class="head">お客様の声</li><li class="head">お問い合わせ</li><li class="head">プライバシーポリシー</li></ul>
<div class="abs footer-bar">© SORANOMICHI TOUR. ALL RIGHTS RESERVED.</div>
</footer>

</body>
</html>
```